Vent doux

Hello,
I’m a designer sunglasses reatail Store owner in Montreal, Quebec.

Looking for something modern, fresh with a trendy appeal.

Will send my logo.
Thank you.

Store

```html
<!DOCTYPE html>
<html lang="fr">
<head>
<meta charset="utf-8">
<title>Vent doux — cartes professionnelles</title>
<link href="https://fonts.googleapis.com/css2?family=Lato:wght@400;700&family=Exo+2:wght@400&display=swap" rel="stylesheet">
<style>
  :root {
    --bg: #333333;
    --crimson: #9b1730;
    --ink: #222222;
    --grey: #5a5a5a;
    --paper: #ffffff;
    --faint: #ececec;
    --dark-slash: #2b2b2b;
  }
  * { box-sizing: border-box; margin: 0; padding: 0; }
  html, body { width: 1200px; height: 900px; overflow: hidden; }
  body {
    background: var(--bg);
    font-family: "Lato", Arial, sans-serif;
    position: relative;
  }
  .card {
    position: absolute;
    width: 540px;
    height: 310px;
    top: 295px;
    overflow: hidden;
    box-shadow: 0 12px 28px rgba(0,0,0,.45);
  }
  /* Front */
  .card-front { left: 40px; background: var(--paper); }
  .contact-name {
    position: absolute; left: 34px; top: 30px;
    color: var(--crimson); font-weight: 700; font-size: 20px;
  }
  .contact-role {
    position: absolute; left: 34px; top: 55px;
    color: var(--ink); font-size: 12px;
  }
  .contact-details {
    position: absolute; left: 34px; top: 100px;
    color: var(--ink); font-size: 12.5px; line-height: 17px; list-style: none;
  }
  .contact-details li { display: flex; align-items: center; gap: 6px; }
  .contact-details svg { width: 11px; height: 11px; fill: var(--crimson); }
  .contact-details .plain { padding-left: 0; }
  .brand {
    position: absolute; left: 268px; top: 110px;
  }
  .brand-row { display: flex; align-items: center; gap: 10px; }
  .brand-dot {
    width: 26px; height: 26px; border-radius: 50%; background: var(--crimson);
  }
  .brand-name {
    font-family: "Lato", Arial, sans-serif; font-weight: 700;
    font-size: 38px; color: var(--ink); line-height: 1;
  }
  .brand-tagline {
    font-family: "Exo 2", Arial, sans-serif; font-size: 12px;
    letter-spacing: 3px; color: var(--grey); margin: 6px 0 0 36px;
  }
  .faint-circle {
    position: absolute; left: 330px; top: 180px;
    width: 120px; height: 120px; border-radius: 50%;
    border: 14px solid var(--faint);
  }
  .front-band {
    position: absolute; left: 0; bottom: 14px; width: 100%; height: 28px;
  }
  .front-band svg { display: block; width: 100%; height: 100%; }
  .band-url {
    position: absolute; left: 34px; bottom: 20px;
    color: var(--paper); font-size: 13px;
  }
  /* Back */
  .card-back {
    left: 620px; background: var(--crimson);
    display: flex; flex-direction: column; align-items: center; justify-content: center;
  }
  .card-back .brand-name { color: var(--paper); font-size: 44px; }
  .card-back .brand-dot { background: var(--paper); width: 30px; height: 30px; }
  .card-back .brand-tagline { color: var(--paper); margin-left: 40px; }
  .back-url {
    margin-top: 38px; color: var(--paper); font-size: 14px; letter-spacing: .5px;
  }
</style>
</head>
<body>

<section class="card card-front" aria-label="Recto de la carte">
  <p class="contact-name">Julien Marchand</p>
  <p class="contact-role">Owner</p>
  <ul class="contact-details">
    <li class="plain">845 rue des Érables</li>
    <li class="plain">Montréal (Qc) H3K 2B7</li>
    <li><svg viewBox="0 0 12 12"><path d="M3 1l2 2-1 1.5c.6 1.4 1.6 2.4 3 3L8.5 6.5l2 2L9 11C5 10.5 1.5 7 1 3z"/></svg>514 555-0142</li>
    <li><svg viewBox="0 0 12 12"><rect x="3" y="0.5" width="6" height="11" rx="1"/></svg>514 555-0187</li>
    <li><svg viewBox="0 0 12 12"><path d="M0 2h12v8H0z M1 3l5 3.5L11 3" /></svg>info@ventdoux.com</li>
  </ul>

  <div class="brand">
    <div class="brand-row">
      <span class="brand-dot"></span>
      <span class="brand-name">Vent doux</span>
    </div>
    <p class="brand-tagline">lunettes &amp; accessoires</p>
  </div>

  <div class="faint-circle" aria-hidden="true"></div>

  <div class="front-band" aria-hidden="true">
    <svg viewBox="0 0 540 28" preserveAspectRatio="none">
      <polygon points="0,0 440,0 430,28 0,28" fill="var(--crimson)"/>
      <polygon points="450,0 488,0 478,28 440,28" fill="var(--dark-slash)"/>
      <polygon points="498,0 540,0 540,28 488,28" fill="var(--crimson)"/>
    </svg>
  </div>
  <p class="band-url">www.ventdoux.com</p>
</section>

<section class="card card-back" aria-label="Verso de la carte">
  <div class="brand-row">
    <span class="brand-dot"></span>
    <span class="brand-name">Vent doux</span>
  </div>
  <p class="brand-tagline">lunettes &amp; accessoires</p>
  <p class="back-url">www.ventdoux.com</p>
</section>

</body>
</html>
```